New business card with our logo

we finalized our logo with the help of pixel harbor - now we need a business card using that logo. we are a metal service center providing raw steel and metal products for fabricating, contractors, artists, etc. we have the wording for the back of the card figured out (attached, no deviations from text please), just need help putting it all together.
would like the look of steel somehow incorporated in the design ... would like the black part of the logo to be steel or silver color (the S & BRANLEY)
Other font styles liked:
- calibri, arial, similar to those, modern looking
Colors
Designer to choose colors to be used in the design.
Requirements
Must have
- Back of card must haves are attached (no deviations from wording please).
- FRONT of card:
- logo
- address
- name
- office tel
- cell
- fax
- website
- address
Nice to have
- incorporate the look of steel or element of steel somehow
- names of the staff on front not in all caps, i.e. Rosvita not ROSVITA
- this industry is more industrial, not coffee or flower shop so design should be aligned with that
- design should be classic and tasteful

```html
<!DOCTYPE html>
<html lang="en">
<head>
<meta charset="utf-8">
<title>Branley Steel – Business Card</title>
<link href="https://fonts.googleapis.com/css2?family=Open+Sans:wght@400;600;700&display=swap" rel="stylesheet">
<style>
  :root {
    --bg-dark: #2a2c2f;
    --bg-light: #4a4d51;
    --card-black: #1f1d1e;
    --steel-light: #e6e8ea;
    --steel-mid: #b9bcbf;
    --steel-dark: #8d9094;
    --accent-blue: #1f74c9;
    --text-white: #ffffff;
    --text-soft: #e4e4e4;
    --ring-faint: #2f2d2e;
  }
  * { margin: 0; padding: 0; box-sizing: border-box; }
  html, body { width: 1200px; height: 900px; overflow: hidden; }
  body {
    font-family: "Open Sans", Arial, sans-serif;
    background: radial-gradient(ellipse at 60% 40%, var(--bg-light), var(--bg-dark) 75%);
    position: relative;
  }
  .card {
    position: absolute;
    width: 560px;
    height: 320px;
    border-radius: 22px;
    overflow: hidden;
    box-shadow: 0 18px 40px rgba(0,0,0,.45);
  }

  /* Steel side */
  .card--steel {
    left: 60px; top: 90px;
    background:
      repeating-linear-gradient(0deg, rgba(255,255,255,.05) 0 1px, rgba(0,0,0,.04) 1px 2px),
      linear-gradient(115deg, var(--steel-dark) 0%, var(--steel-light) 22%, var(--steel-mid) 38%, var(--steel-light) 55%, var(--steel-dark) 72%, var(--steel-mid) 100%);
    display: flex; flex-direction: column; align-items: center; justify-content: center;
  }
  .steel-brand { display: flex; align-items: center; gap: 14px; }
  .brand-dot {
    width: 46px; height: 46px; border-radius: 50%;
    border: 5px solid var(--text-white);
  }
  .steel-brand .brand-name {
    font-weight: 700; font-size: 40px; color: var(--text-white); letter-spacing: .5px;
  }
  .steel-url { margin-top: 6px; font-size: 17px; color: var(--text-white); letter-spacing: 1px; }

  /* Dark side */
  .card--dark {
    left: 580px; top: 490px;
    background: var(--card-black);
    color: var(--text-white);
  }
  .faint-ring {
    position: absolute; right: -30px; top: 10px;
    width: 300px; height: 300px; border-radius: 50%;
    border: 16px solid var(--ring-faint);
  }
  .dark-brand {
    position: absolute; left: 28px; top: 30px;
    display: flex; align-items: center; gap: 10px;
  }
  .dark-brand .brand-dot { width: 34px; height: 34px; border-width: 4px; border-color: var(--accent-blue); }
  .dark-brand .brand-name { font-weight: 700; font-size: 26px; color: var(--text-white); }
  .address { position: absolute; left: 32px; top: 84px; font-size: 13px; line-height: 1.35; color: var(--text-soft); }
  .contact-list { position: absolute; left: 32px; bottom: 26px; list-style: none; }
  .contact-list li {
    display: flex; align-items: center; gap: 12px;
    font-size: 14px; line-height: 22px; color: var(--text-soft);
  }
  .contact-list svg { width: 14px; height: 14px; fill: var(--accent-blue); flex: none; }

  .services { position: absolute; right: 36px; top: 30px; width: 270px; text-align: right; }
  .services-title { font-weight: 700; font-size: 18px; color: var(--accent-blue); letter-spacing: .4px; }
  .services-ops { font-size: 12px; color: var(--text-soft); margin-top: 2px; }
  .services-rule { height: 1.5px; background: var(--text-white); margin: 6px 0 6px 40px; }
  .services-list { font-size: 11.5px; line-height: 1.4; color: var(--text-soft); }

  .person {
    position: absolute; right: 36px; bottom: 80px; text-align: right;
    border-right: 2px solid var(--text-white); padding-right: 10px;
  }
  .person-name { font-size: 24px; font-weight: 600; line-height: 1.1; }
  .person-name .first { color: var(--accent-blue); }
  .person-name .last { color: var(--text-white); }
  .person-role { font-size: 12px; color: var(--text-soft); }
</style>
</head>
<body>

<section class="card card--steel" aria-label="Card front, brushed steel">
  <div class="steel-brand">
    <span class="brand-dot"></span>
    <span class="brand-name">BRANLEY STEEL</span>
  </div>
  <p class="steel-url">www.branleysteel.com</p>
</section>

<section class="card card--dark" aria-label="Card back, contact details">
  <div class="faint-ring"></div>

  <div class="dark-brand">
    <span class="brand-dot"></span>
    <span class="brand-name">BRANLEY STEEL</span>
  </div>
  <p class="address">2218 Birch Avenue<br>Elmhurst, Illinois 60126</p>

  <ul class="contact-list">
    <li><svg viewBox="0 0 24 24"><path d="M6.6 10.8a15.1 15.1 0 0 0 6.6 6.6l2.2-2.2a1 1 0 0 1 1-.25 11.4 11.4 0 0 0 3.6.57 1 1 0 0 1 1 1V20a1 1 0 0 1-1 1A17 17 0 0 1 3 4a1 1 0 0 1 1-1h3.5a1 1 0 0 1 1 1c0 1.25.2 2.45.57 3.57a1 1 0 0 1-.25 1z"/></svg>630-555-0147</li>
    <li><svg viewBox="0 0 24 24"><path d="M7 1h10a2 2 0 0 1 2 2v18a2 2 0 0 1-2 2H7a2 2 0 0 1-2-2V3a2 2 0 0 1 2-2zm0 3v15h10V4z"/></svg>630-555-0147</li>
    <li><svg viewBox="0 0 24 24"><path d="M6 2h9l3 3v4h2a2 2 0 0 1 2 2v9a2 2 0 0 1-2 2H4a2 2 0 0 1-2-2v-9a2 2 0 0 1 2-2h2zm2 2v5h8V6h-3V4zm-2 9v2h2v-2zm4 0v2h2v-2zm4 0v2h2v-2z"/></svg>630-555-0148</li>
    <li><svg viewBox="0 0 24 24"><path d="M2 5h20v14H2zm2 2v.5l8 5 8-5V7l-8 5z"/></svg>info@branleysteel.com</li>
    <li><svg viewBox="0 0 24 24"><path d="M12 2a10 10 0 1 0 0 20 10 10 0 0 0 0-20zm6.9 9h-3a15 15 0 0 0-1.3-5.6A8 8 0 0 1 18.9 11zM12 4c.9 1.2 1.8 3.6 1.9 7h-3.8c.1-3.4 1-5.8 1.9-7zM9.4 5.4A15 15 0 0 0 8.1 11h-3a8 8 0 0 1 4.3-5.6zM5.1 13h3a15 15 0 0 0 1.3 5.6A8 8 0 0 1 5.1 13zM12 20c-.9-1.2-1.8-3.6-1.9-7h3.8c-.1 3.4-1 5.8-1.9 7zm2.6-1.4a15 15 0 0 0 1.3-5.6h3a8 8 0 0 1-4.3 5.6z"/></svg>www.branleysteel.com</li>
  </ul>

  <div class="services">
    <p class="services-title">METAL SERVICE CENTER</p>
    <p class="services-ops">Cut | Shear | Punch | Light Fab</p>
    <div class="services-rule"></div>
    <p class="services-list">Structural Steel | Stainless &amp; Aluminum<br>Building Components | Rebar | Decking<br>and more...</p>
  </div>

  <div class="person">
    <p class="person-name"><span class="first">Rosvita</span> <span class="last">Kessler</span></p>
    <p class="person-role">CEO &amp; Founder</p>
  </div>
</section>

</body>
</html>
```